Advertising company unique advertising platform

we need a logo design for a new company based in Australia Melbourne. We develop innovated advertising platform where consumer can use this platform to get regular discount, as business owner they can use this platform for free advertisement. Payment for this advertisement platform only payable every two weeks, when I generate revenue for their business

Industry/Entity Type

Advertising

Contact Information for Business Card

Dale Pruitt | Co-Founder |Managing Director
Suite 718 263 Harrowgate Row Melbourne Vic 3000

ABN 41 902 615 273
Tel: +61 0491 528 307 | Email: dale.pruitt@corvelaxtro.com

Font styles to use
Decorative
Script

Requirements
Must have
• Try few different design and some round corner business card
Should not have
• One round corner business card...try 4 different colour background not only black, make sure two side is designed. Be creative so imagine you are giving this to a client make sure has wow factor, if you can also try one design with engrave like all the logo, words look 3d feel
• The word Advertising Platform use attached file font

```html
<!DOCTYPE html>
<html lang="en">
<head>
<meta charset="utf-8">
<title>Tallowfern Exchange — Business Card</title>
<link rel="stylesheet" href="https://fonts.googleapis.com/css2?family=Cinzel:wght@400;600&family=Poppins:wght@400;500&display=swap">
<style>
  :root {
    --canvas: #d9d4cc;
    --card-black: #050505;
    --card-sheen: #1c1c1c;
    --accent-orange: #f0862a;
    --text-white: #f4f4f4;
    --rule-grey: #8a8a8a;
  }
  * { box-sizing: border-box; margin: 0; padding: 0; }
  html, body {
    width: 1200px; height: 900px; overflow: hidden;
    background: var(--canvas);
  }
  .sheet {
    width: 1200px; height: 900px;
    display: flex; flex-direction: column;
    align-items: center; justify-content: center;
    gap: 60px;
  }
  .card {
    position: relative;
    width: 665px; height: 380px;
    border-radius: 26px;
    background: linear-gradient(125deg, var(--card-black) 0%, var(--card-sheen) 48%, var(--card-black) 62%, var(--card-black) 100%);
    box-shadow: 0 10px 28px rgba(0,0,0,0.35);
    overflow: hidden;
  }
  .brand {
    display: flex; align-items: center; gap: 14px;
    font-family: "Cinzel", serif;
    font-weight: 600;
    color: var(--accent-orange);
    letter-spacing: 0.04em;
    line-height: 1.1;
  }
  .brand-dot {
    flex: none;
    width: 46px; height: 46px;
    border-radius: 50%;
    background: var(--accent-orange);
  }
  .card-front .brand {
    position: absolute; left: 50%; top: 50%;
    transform: translate(-50%, -50%);
    font-size: 34px;
  }
  .card-back .brand {
    position: absolute; left: 48px; top: 50%;
    transform: translateY(-50%);
    font-size: 28px;
    width: 260px;
  }
  .card-back .brand-dot { width: 38px; height: 38px; }
  .details {
    position: absolute; left: 350px; top: 70px;
    color: var(--text-white);
  }
  .name-block {
    position: relative;
    padding-left: 22px;
  }
  .name-block::before {
    content: ""; position: absolute; left: 0; top: 8px;
    width: 1px; height: 44px; background: var(--rule-grey);
  }
  .person-name {
    font-family: "Cinzel", serif; font-weight: 400;
    font-size: 30px; color: var(--accent-orange);
    letter-spacing: 0.03em;
  }
  .person-title {
    font-family: "Cinzel", serif; font-size: 10.5px;
    letter-spacing: 0.02em; margin-top: 2px;
  }
  .contact-block {
    position: relative;
    margin-top: 26px; padding-left: 48px;
    font-family: "Poppins", sans-serif; font-size: 14px;
    line-height: 1.5;
  }
  .contact-block::before {
    content: ""; position: absolute; left: 22px; top: 4px;
    width: 1.5px; height: 138px; background: var(--accent-orange);
  }
  .contact-line { display: flex; align-items: center; gap: 8px; }
  .label { color: var(--accent-orange); }
  .icon { width: 13px; height: 13px; flex: none; }
</style>
</head>
<body>
<main class="sheet">
  <section class="card card-front" aria-label="Card front">
    <div class="brand"><span class="brand-dot"></span><span>Tallowfern<br>Exchange</span></div>
  </section>

  <section class="card card-back" aria-label="Card back">
    <div class="brand"><span class="brand-dot"></span><span>Tallowfern<br>Exchange</span></div>
    <div class="details">
      <div class="name-block">
        <h1 class="person-name">DALE PRUITT</h1>
        <p class="person-title">|CO-FOUNDER | MANAGING DIRECTOR</p>
      </div>
      <div class="contact-block">
        <p class="contact-line">Suite 718 263 Harrowgate Row</p>
        <p class="contact-line">Melbourne Vic 3000</p>
        <p class="contact-line"><span class="label">ABN:</span> 41 902 615 273</p>
        <p class="contact-line">
          <svg class="icon" viewBox="0 0 24 24" aria-hidden="true"><path fill="var(--accent-orange)" d="M6.6 10.8a15.1 15.1 0 0 0 6.6 6.6l2.2-2.2a1 1 0 0 1 1-.25 11.4 11.4 0 0 0 3.6.57 1 1 0 0 1 1 1V20a1 1 0 0 1-1 1A17 17 0 0 1 3 4a1 1 0 0 1 1-1h3.5a1 1 0 0 1 1 1c0 1.25.2 2.45.57 3.57a1 1 0 0 1-.25 1z"/></svg>
          +61 0491 528 307
        </p>
        <p class="contact-line">
          <svg class="icon" viewBox="0 0 24 24" aria-hidden="true"><rect x="3" y="5" width="18" height="14" rx="2" fill="none" stroke="var(--accent-orange)" stroke-width="2"/><path d="M3 7l9 6 9-6" fill="none" stroke="var(--accent-orange)" stroke-width="2"/></svg>
          dale.pruitt@corvelaxtro.com
        </p>
      </div>
    </div>
  </section>
</main>
</body>
</html>
```